BrimKeel conversion company design.

Hi,

We specialise in attic/roof conversions to create more space. We have a logo design which we are happy with. We would like someone to design a wrap that will be suitable to be transferred onto a 2008 Corva 310. This is our first car to be wrapped and is what we require a design for.

However, we would like to see a design that can be utilised on a KT Selvano, and 2021 Marelle Haulan van. (I understand the design would change to suit but I would like something that will still look similar when they are sat next to one another).

We have a white background on the car so that would need consideration.

We want something that is noticeable but looks professional.

We will also require are contact information on the design:

email: admin@brimkeel.com.au
Website: brimkeel.com.au
Tel: 1300847162
Social media icons- Glimmora, Kindlyst, Tacklore, Zelvo

Please let me know if you require any further detail.

```html
<!DOCTYPE html>
<html lang="en">
<head>
<meta charset="utf-8">
<title>BrimKeel vehicle wrap</title>
<link rel="stylesheet" href="https://fonts.googleapis.com/css2?family=Montserrat:wght@400;600&family=Oswald:wght@500&display=swap">
<style>
  :root {
    --navy: #13283a;
    --blue: #1b7bc4;
    --white: #f4f4f2;
    --page: #ffffff;
  }
  html, body {
    margin: 0;
    width: 1026px;
    height: 1200px;
    overflow: hidden;
    background: var(--page);
  }
  .wrap-sheet {
    display: flex;
    flex-direction: column;
    align-items: center;
    gap: 70px;
    padding-top: 75px;
  }
  .wrap-panel { display: block; width: 900px; height: 300px; }
  .panel-base { fill: var(--white); }
  .navy-field { fill: var(--navy); }
  .blue-swoosh { fill: var(--blue); }
  .blue-edge { fill: none; stroke: var(--blue); stroke-width: 7; }
  .brand-name {
    font-family: "Montserrat", sans-serif;
    font-weight: 600;
    font-size: 50px;
    fill: var(--navy);
  }
  .brand-mark { fill: var(--blue); }
  .tagline {
    font-family: "Montserrat", sans-serif;
    font-weight: 400;
    font-size: 15px;
    fill: var(--navy);
  }
  .tagline-rule { stroke: var(--blue); stroke-width: 2; }
  .phone {
    font-family: "Oswald", sans-serif;
    font-weight: 500;
    font-size: 58px;
    fill: var(--white);
  }
  .contact-line {
    font-family: "Oswald", sans-serif;
    font-weight: 500;
    font-size: 13px;
    fill: var(--white);
  }
  .social-ring { fill: none; stroke: var(--white); stroke-width: 3; }
  .social-name {
    font-family: "Montserrat", sans-serif;
    font-weight: 400;
    font-size: 14px;
    fill: var(--white);
  }
</style>
</head>
<body>
<main class="wrap-sheet">

  <svg class="wrap-panel" viewBox="0 0 900 300" aria-label="Corva 310 wrap layout">
    <defs>
      <clipPath id="panel-clip"><rect width="900" height="300" rx="28"/></clipPath>
    </defs>
    <g clip-path="url(#panel-clip)">
      <rect class="panel-base" width="900" height="300"/>
      <path class="blue-edge" d="M610 -5 C568 30 556 80 563 140 C571 200 588 262 520 305"/>
      <path class="navy-field" d="M622 0 H900 V300 H540 C600 280 582 200 574 140 C567 82 582 30 622 0 Z"/>
      <path class="blue-swoosh" d="M0 248 C210 212 420 232 590 296 L560 300 C400 258 200 250 0 266 Z"/>
      <path class="navy-field" d="M0 274 C200 256 380 262 545 300 H0 Z"/>
    </g>
    <circle class="brand-mark" cx="170" cy="138" r="10"/>
    <text class="brand-name" x="190" y="156">BrimKeel</text>
    <text class="tagline" x="310" y="190" text-anchor="middle">Storage • Skylights • Conversions</text>
    <line class="tagline-rule" x1="250" y1="204" x2="370" y2="204"/>
    <text class="phone" x="885" y="88" text-anchor="end">1300847162</text>
    <text class="contact-line" x="885" y="112" text-anchor="end">ADMIN@BRIMKEEL.COM.AU  |  WWW.BRIMKEEL.COM.AU</text>
    <circle class="social-ring" cx="630" cy="160" r="18"/><text class="social-name" x="656" y="165">Kindlyst</text>
    <circle class="social-ring" cx="760" cy="160" r="18"/><text class="social-name" x="786" y="165">Zelvo</text>
    <circle class="social-ring" cx="630" cy="214" r="18"/><text class="social-name" x="656" y="219">Tacklore</text>
    <circle class="social-ring" cx="760" cy="214" r="18"/><text class="social-name" x="786" y="219">Glimmora</text>
  </svg>

  <svg class="wrap-panel" viewBox="0 0 900 300" aria-label="KT Selvano wrap layout">
    <defs>
      <clipPath id="panel-clip-ute"><rect width="900" height="300" rx="20"/></clipPath>
    </defs>
    <g clip-path="url(#panel-clip-ute)">
      <rect class="panel-base" width="900" height="300"/>
      <path class="blue-edge" d="M470 -5 C440 40 440 90 452 140 C462 200 470 260 420 305"/>
      <path class="navy-field" d="M482 0 H900 V300 H440 C490 275 478 200 466 140 C455 85 455 35 482 0 Z"/>
      <path class="blue-swoosh" d="M0 240 C190 208 360 228 480 292 L455 300 C330 252 180 246 0 258 Z"/>
      <path class="navy-field" d="M0 268 C180 252 330 262 440 300 H0 Z"/>
    </g>
    <circle class="brand-mark" cx="95" cy="138" r="10"/>
    <text class="brand-name" x="115" y="156">BrimKeel</text>
    <text class="tagline" x="235" y="190" text-anchor="middle">Storage • Skylights • Conversions</text>
    <line class="tagline-rule" x1="175" y1="204" x2="295" y2="204"/>
    <text class="phone" x="885" y="92" text-anchor="end">1300847162</text>
    <text class="contact-line" x="885" y="116" text-anchor="end">ADMIN@BRIMKEEL.COM.AU  |  WWW.BRIMKEEL.COM.AU</text>
    <circle class="social-ring" cx="630" cy="170" r="18"/><text class="social-name" x="656" y="175">Kindlyst</text>
    <circle class="social-ring" cx="760" cy="170" r="18"/><text class="social-name" x="786" y="175">Zelvo</text>
    <circle class="social-ring" cx="630" cy="224" r="18"/><text class="social-name" x="656" y="229">Tacklore</text>
    <circle class="social-ring" cx="760" cy="224" r="18"/><text class="social-name" x="786" y="229">Glimmora</text>
  </svg>

  <svg class="wrap-panel" viewBox="0 0 900 300" aria-label="Marelle Haulan wrap layout">
    <defs>
      <clipPath id="panel-clip-van"><rect width="900" height="300" rx="24"/></clipPath>
    </defs>
    <g clip-path="url(#panel-clip-van)">
      <rect class="panel-base" width="900" height="300"/>
      <path class="blue-edge" d="M720 -3 C600 10 560 60 560 130 C560 200 590 260 520 305"/>
      <path class="navy-field" d="M740 0 H900 V300 H545 C610 270 578 200 578 135 C578 65 620 15 740 0 Z"/>
      <path class="blue-swoosh" d="M0 236 C210 200 420 222 590 294 L560 300 C400 250 200 242 0 256 Z"/>
      <path class="navy-field" d="M0 268 C200 250 380 260 545 300 H0 Z"/>
    </g>
    <circle class="brand-mark" cx="175" cy="138" r="10"/>
    <text class="brand-name" x="195" y="156">BrimKeel</text>
    <text class="tagline" x="315" y="190" text-anchor="middle">Storage • Skylights • Conversions</text>
    <line class="tagline-rule" x1="255" y1="204" x2="375" y2="204"/>
    <text class="phone" x="885" y="94" text-anchor="end">1300847162</text>
    <text class="contact-line" x="885" y="118" text-anchor="end">ADMIN@BRIMKEEL.COM.AU  |  WWW.BRIMKEEL.COM.AU</text>
    <circle class="social-ring" cx="630" cy="170" r="18"/><text class="social-name" x="656" y="175">Kindlyst</text>
    <circle class="social-ring" cx="760" cy="170" r="18"/><text class="social-name" x="786" y="175">Zelvo</text>
    <circle class="social-ring" cx="630" cy="224" r="18"/><text class="social-name" x="656" y="229">Tacklore</text>
    <circle class="social-ring" cx="760" cy="224" r="18"/><text class="social-name" x="786" y="229">Glimmora</text>
  </svg>

</main>
</body>
</html>
```